ultra-minimalist business card

front (black background, matte):

tarik b. hosseny
writer | photographer
get@tarikhosseny.com

back (white background, matte):

a picture speaks a thousand words;
a word draws a thousand pictures.

www.tarikhosseny.com

all text should be small (white or silver - as long as it shows against the black - on the front; black or gray - as long as it shows against the white - on the back).

feel free to get creative in terms of arrangement, alignment, and font type, but remember, the overall style is minimalist, so nothing too fancy, please.

thanks.

```html
<!DOCTYPE html>
<html lang="en">
<head>
<meta charset="utf-8">
<title>Business card – tarik b. hosseny</title>
<link rel="stylesheet" href="https://fonts.googleapis.com/css2?family=PT+Sans:wght@400;700&family=Courier+Prime:ital,wght@0,400;0,700;1,400&display=swap">
<style>
  :root {
    --sheet: #ffffff;
    --card-front: #000000;
    --card-back: #ffffff;
    --ink-black: #000000;
    --ink-white: #ffffff;
    --ink-silver: #c8c8c8;
    --ink-30: #b3b3b3;
    --ink-60: #666666;
    --sans: "PT Sans", Tahoma, sans-serif;
    --mono: "Courier Prime", "Courier New", monospace;
  }
  html, body {
    margin: 0;
    padding: 0;
    width: 1200px;
    height: 848px;
    overflow: hidden;
    background: var(--sheet);
  }
  .sheet {
    position: relative;
    width: 1200px;
    height: 848px;
  }
  .card {
    position: absolute;
    width: 364px;
    height: 202px;
    box-sizing: border-box;
    text-align: center;
  }
  .card--front { background: var(--card-front); }
  .card--back { background: var(--card-back); border: 2px solid var(--ink-black); }
  .row-1 { top: 194px; }
  .row-2 { top: 415px; }
  .col-front { left: 228px; }
  .col-back { left: 608px; }

  .line {
    position: absolute;
    left: 0;
    right: 0;
    margin: 0;
    line-height: 1;
    white-space: nowrap;
  }
  .name {
    top: 63px;
    font-family: var(--sans);
    font-weight: 700;
    font-size: 14.5px;
  }
  .role {
    top: 80px;
    font-family: var(--mono);
    font-style: italic;
    font-size: 12.7px;
  }
  .email {
    top: 125px;
    font-family: var(--sans);
    font-size: 13.5px;
  }
  .quote {
    top: 64px;
    font-family: var(--mono);
    font-weight: 700;
    font-size: 12.7px;
    line-height: 15px;
  }
  .web {
    top: 128px;
    font-family: var(--sans);
    font-size: 13.5px;
  }
  .card--back .quote, .card--back .web { top: auto; }
  .card--back .quote { top: 62px; }
  .card--back .web { top: 126px; }

  .tone-full .name, .tone-full .email { color: var(--ink-white); }
  .tone-full .role { color: var(--ink-silver); }
  .tone-30 .name, .tone-30 .email, .tone-30 .role { color: var(--ink-30); }
  .tone-black .quote, .tone-black .web { color: var(--ink-black); }
  .tone-60 .quote, .tone-60 .web { color: var(--ink-60); }

  .caption {
    position: absolute;
    top: 636px;
    width: 364px;
    margin: 0;
    text-align: center;
    font-family: var(--mono);
    font-weight: 700;
    font-size: 12.8px;
    color: var(--ink-black);
    white-space: nowrap;
  }
  .caption--front { left: 206px; }
  .caption--back { left: 615px; }
</style>
</head>
<body>
<main class="sheet">
  <section class="card card--front row-1 col-front tone-full" aria-label="Front, full white text">
    <p class="line name">tarik b. hosseny</p>
    <p class="line role">writer | photographer</p>
    <p class="line email">get@tarikhosseny.com</p>
  </section>

  <section class="card card--back row-1 col-back tone-black" aria-label="Back, black text">
    <p class="line quote">a picture speaks a thousand words;<br>a word draws a thousand pictures.</p>
    <p class="line web">www.tarikhosseny.com</p>
  </section>

  <section class="card card--front row-2 col-front tone-30" aria-label="Front, 30% black text">
    <p class="line name">tarik b. hosseny</p>
    <p class="line role">writer | photographer</p>
    <p class="line email">get@tarikhosseny.com</p>
  </section>

  <section class="card card--back row-2 col-back tone-60" aria-label="Back, 60% black text">
    <p class="line quote">a picture speaks a thousand words;<br>a word draws a thousand pictures.</p>
    <p class="line web">www.tarikhosseny.com</p>
  </section>

  <p class="caption caption--front">Font colour - 30% black</p>
  <p class="caption caption--back">Font colour - 60% black</p>
</main>
</body>
</html>
```